Yoga Instrucor

I need my personal business cards, i would like the front a kind of light but vibrant red and matt gold.

Industry/Entity Type

Business

Contact Information for Business Card

Rosalind Quenneby
Yoga Instructor
RYT 200, PRAVO (NYC) Yoga RYT 500,
CPR/ AED Certified,
quennebyrosalind@mailvista.net
512 804 6193
Adult Yoga, Private Yoga, Group Classes, Restorative, Meditation, Child Yoga.

```html
<!DOCTYPE html>
<html lang="en">
<head>
<meta charset="utf-8">
<title>Rosalind Quenneby Yoga – Business Cards</title>
<link rel="stylesheet" href="https://fonts.googleapis.com/css2?family=Didact+Gothic&family=Nunito+Sans:wght@800&display=swap">
<style>
  :root {
    --backdrop: #1b1b1c;
    --vibrant-red: #d42a5b;
    --red-soft: #c4426c;
    --matt-gold: #f0cd72;
    --card-white: #f4f4f4;
    --card-white-edge: #e6e6e6;
    --ink: #3a3a3a;
  }
  * { box-sizing: border-box; margin: 0; padding: 0; }
  html, body {
    width: 1200px; height: 1000px; overflow: hidden;
    background: var(--backdrop);
    font-family: "Didact Gothic", "Century Gothic", sans-serif;
  }
  .sheet {
    position: relative; width: 1200px; height: 1000px;
    display: flex; flex-direction: column; align-items: center; justify-content: center; gap: 60px;
  }
  .card {
    position: relative; width: 700px; height: 400px; overflow: hidden;
    box-shadow: 0 18px 40px rgba(0,0,0,.55);
  }
  /* Front */
  .card-front {
    background: linear-gradient(160deg, var(--vibrant-red) 0%, #d02756 45%, var(--red-soft) 100%);
    display: flex; align-items: center; justify-content: center;
  }
  .brand-name {
    font-family: "Didact Gothic", "Century Gothic", sans-serif;
    font-weight: 400; letter-spacing: 1px;
  }
  .card-front .brand-name { color: var(--matt-gold); font-size: 50px; }
  /* Back */
  .card-back {
    background: linear-gradient(170deg, #ffffff 0%, var(--card-white) 55%, var(--card-white-edge) 100%);
  }
  .card-back .brand-name {
    position: absolute; top: 40px; right: 40px;
    color: var(--vibrant-red); font-size: 30px;
  }
  .holder {
    position: absolute; top: 82px; left: 56px;
  }
  .holder-name {
    font-family: "Nunito Sans", sans-serif; font-weight: 800;
    color: var(--vibrant-red); font-size: 22px; line-height: 1.1;
  }
  .holder-role { color: var(--ink); font-size: 15px; margin-top: 2px; }
  .gold-rule {
    position: absolute; top: 126px; left: 290px; right: 0;
    height: 4px; background: var(--matt-gold);
  }
  .details {
    position: absolute; top: 160px; left: 90px;
    list-style: none; color: var(--ink); font-size: 17px; line-height: 29px;
  }
  .services {
    position: absolute; left: 0; right: 0; bottom: 0; height: 78px;
    background: linear-gradient(90deg, var(--vibrant-red), var(--red-soft) 60%, #c63a6a);
    color: var(--matt-gold); font-size: 17px;
    display: flex; align-items: center; justify-content: center;
  }
</style>
</head>
<body>
<main class="sheet">
  <section class="card card-front" aria-label="Card front">
    <div class="brand-name">Rosalind Quenneby</div>
  </section>

  <section class="card card-back" aria-label="Card back">
    <div class="brand-name">Rosalind Quenneby</div>
    <div class="holder">
      <div class="holder-name">Rosalind Quenneby</div>
      <div class="holder-role">Yoga Instructor</div>
    </div>
    <div class="gold-rule"></div>
    <ul class="details">
      <li>RYT 200, PRAVO (NYC) Yoga RYT 500</li>
      <li>CPR/ AED Certified</li>
      <li>p: 512 804 6193</li>
      <li>e: quennebyrosalind@mailvista.net</li>
    </ul>
    <div class="services">Adult Yoga, Private Yoga, Group Classes, Restorative, Meditation, Child Yoga.</div>
  </section>
</main>
</body>
</html>
```